Bref créative
business cards & stationary
Corvell Insulation
Modern
BO KERRIGAN
SALESMAN
14 PELLMORE CT.
MARLOW, CA 95410
bo.kerrigan@corvellinsulation.com
www.corvellinsulation.com
I'd like the edges to be rounded instead of pointed. I would also like little symbols next to the phone, E-mail, website, and fax. For example, near the phone number, a small telephone. Also, if possible, I would like a QR Barcode that leads to my website on the back.

```html
<!DOCTYPE html>
<html lang="en">
<head>
<meta charset="utf-8">
<title>Corvell Insulation – Business Cards</title>
<link href="https://fonts.googleapis.com/css2?family=Exo+2:wght@400;600;700&display=swap" rel="stylesheet">
<style>
  :root {
    --bg: #e4e4e2;
    --card: #ffffff;
    --green: #3aa935;
    --green-light: #8cd13a;
    --green-dark: #1f7a22;
    --ink: #3a3a3a;
    --ink-soft: #6a6a6a;
    --stripe: #3b3b3b;
  }
  * { box-sizing: border-box; margin: 0; padding: 0; }
  html, body { width: 1200px; height: 864px; overflow: hidden; }
  body {
    background: var(--bg);
    font-family: "Exo 2", sans-serif;
    display: flex; align-items: center; justify-content: center; gap: 44px;
  }
  .card {
    position: relative;
    width: 540px; height: 309px;
    background: var(--card);
    border-radius: 26px;
    overflow: hidden;
    box-shadow: 0 10px 28px rgba(0,0,0,.18);
  }
  /* Front */
  .card--front { display: flex; align-items: center; justify-content: center; gap: 22px; }
  .brand-mark { width: 64px; height: 64px; background: var(--green); border-radius: 6px; flex: none; }
  .brand-name {
    font-weight: 700; color: var(--ink); line-height: 1;
    font-size: 46px; letter-spacing: 2px; text-transform: uppercase;
  }
  .brand-name span { display: block; font-size: 27px; letter-spacing: 4px; margin-top: 6px; }
  /* Back */
  .swoosh { position: absolute; inset: 0; width: 100%; height: 100%; }
  .back-brand { position: absolute; left: 34px; top: 58px; display: flex; align-items: center; gap: 12px; }
  .back-brand .brand-mark { width: 38px; height: 38px; border-radius: 4px; }
  .back-brand .brand-name { font-size: 27px; letter-spacing: 1px; }
  .back-brand .brand-name span { font-size: 15px; letter-spacing: 2.5px; margin-top: 4px; }
  .person { position: absolute; left: 64px; top: 150px; }
  .person__name { color: var(--green); font-weight: 600; font-size: 15px; letter-spacing: 1.5px; }
  .person__title { color: var(--ink-soft); font-size: 11px; letter-spacing: 2px; margin-top: 3px; }
  .contact {
    position: absolute; left: 290px; top: 54px; list-style: none;
    display: flex; flex-direction: column; gap: 6px;
  }
  .contact li {
    display: flex; align-items: flex-start; gap: 8px;
    font-size: 10.5px; color: var(--ink); letter-spacing: .8px; line-height: 13px;
  }
  .contact li.lower { text-transform: none; letter-spacing: .3px; }
  .contact svg { width: 13px; height: 13px; flex: none; }
</style>
</head>
<body>

<section class="card card--front" aria-label="Card front">
  <div class="brand-mark"></div>
  <div class="brand-name">Corvell<span>Insulation</span></div>
</section>

<section class="card card--back" aria-label="Card back">
  <svg class="swoosh" viewBox="0 0 540 309" preserveAspectRatio="none" aria-hidden="true">
    <defs>
      <linearGradient id="greenSweep" x1="0" y1="1" x2="1" y2="0">
        <stop offset="0" stop-color="var(--green-dark)"/>
        <stop offset=".5" stop-color="var(--green)"/>
        <stop offset="1" stop-color="var(--green-light)"/>
      </linearGradient>
    </defs>
    <path d="M0 200 C120 212 300 228 540 236 L540 309 L0 309 Z" fill="url(#greenSweep)"/>
    <path d="M150 309 C290 270 420 252 540 248 L540 264 C430 268 320 284 215 309 Z" fill="var(--stripe)"/>
    <path d="M215 309 C320 284 430 268 540 264 L540 309 Z" fill="#ffffff"/>
  </svg>

  <div class="back-brand">
    <div class="brand-mark"></div>
    <div class="brand-name">Corvell<span>Insulation</span></div>
  </div>

  <div class="person">
    <p class="person__name">BO KERRIGAN</p>
    <p class="person__title">SALESMAN</p>
  </div>

  <ul class="contact">
    <li>
      <svg viewBox="0 0 14 14"><circle cx="7" cy="7" r="7" fill="var(--green)"/><path d="M7 3a2.4 2.4 0 0 0-2.4 2.4C4.6 7.4 7 10.8 7 10.8s2.4-3.4 2.4-5.4A2.4 2.4 0 0 0 7 3z" fill="#fff"/><circle cx="7" cy="5.4" r=".9" fill="var(--green)"/></svg>
      <span>14 PELLMORE CT.<br>MARLOW, CA 95410</span>
    </li>
    <li>
      <svg viewBox="0 0 14 14"><circle cx="7" cy="7" r="7" fill="var(--green)"/><path d="M4.3 3.6l1.5-.3.8 1.9-.9.7c.5 1 1.2 1.7 2.2 2.2l.7-.9 1.9.8-.3 1.5c-3.3.2-6.1-2.6-5.9-5.9z" fill="#fff"/></svg>
      <span>(555) 402-1187</span>
    </li>
    <li>
      <svg viewBox="0 0 14 14"><circle cx="7" cy="7" r="7" fill="var(--green)"/><rect x="5" y="3" width="4" height="8" rx=".8" fill="#fff"/><rect x="5.7" y="4" width="2.6" height="4.6" fill="var(--green)"/></svg>
      <span>(555) 402-3390</span>
    </li>
    <li>
      <svg viewBox="0 0 14 14"><circle cx="7" cy="7" r="7" fill="var(--green)"/><rect x="4.5" y="3.3" width="5" height="3" fill="#fff"/><rect x="3.3" y="6" width="7.4" height="3.2" rx=".6" fill="#fff"/><rect x="4.5" y="8.6" width="5" height="2.2" fill="#fff" stroke="var(--green)" stroke-width=".5"/></svg>
      <span>(555) 402-7716</span>
    </li>
    <li class="lower">
      <svg viewBox="0 0 14 14"><circle cx="7" cy="7" r="7" fill="var(--green)"/><rect x="3.5" y="4.5" width="7" height="5" fill="#fff"/><path d="M3.5 4.5L7 7.4l3.5-2.9" fill="none" stroke="var(--green)" stroke-width=".8"/></svg>
      <span>bo.kerrigan@corvellinsulation.com</span>
    </li>
    <li class="lower">
      <svg viewBox="0 0 14 14"><circle cx="7" cy="7" r="7" fill="var(--green)"/><circle cx="7" cy="7" r="3.6" fill="none" stroke="#fff" stroke-width=".9"/><ellipse cx="7" cy="7" rx="1.5" ry="3.6" fill="none" stroke="#fff" stroke-width=".8"/><path d="M3.4 7h7.2" stroke="#fff" stroke-width=".8"/></svg>
      <span>www.corvellinsulation.com</span>
    </li>
  </ul>
</section>

</body>
</html>
```